Call for Garage Door Service Label

Design a label to attached to garage doors that has our information for customer to contact us for service. there should be two designs. one that is focused on residential clients, the other is focused on commercial clients. the sticker size should be 5" wide by 4" high. Note for the designer not the label - for more info please visit our website kelz.ca or ask me

Target Market(s)

One for Residential and One for commercial

Industry/Entity Type

Overhead Garage doors

Colors

Designer to choose colors to be used in the design.

Requirements
Must have
• My Logo, My Phone Number (should be large and easy to see), My email sales@kelz.ca, My website www.kelz.ca

```html
<!DOCTYPE html>
<html lang="en">
<head>
<meta charset="utf-8">
<title>Kelz Overhead Door – Service Labels</title>
<link rel="stylesheet" href="https://fonts.googleapis.com/css2?family=Archivo:wght@800&family=Open+Sans:wght@700&family=Roboto+Condensed:wght@700&family=Roboto:wght@400;700&display=swap">
<style>
  :root {
    --backdrop: #c9c7c8;
    --paper: #ffffff;
    --maroon: #5c1d1d;
    --slate: #4f4f4f;
    --ink-light: #ffffff;
  }
  * { margin: 0; padding: 0; box-sizing: border-box; }
  html, body { width: 1200px; height: 1200px; overflow: hidden; }
  body { background: var(--backdrop); position: relative; font-family: "Roboto", Arial, sans-serif; }

  .label {
    position: absolute; left: 297px; width: 605px; height: 490px;
    background: var(--maroon); overflow: hidden;
    box-shadow: 0 4px 14px rgba(0,0,0,.35);
  }
  .label--residential { top: 88px; }
  .label--commercial { top: 624px; }

  .label__brand-area {
    position: absolute; left: 0; top: 0; width: 100%; height: 204px;
    background: var(--paper);
    display: flex; align-items: center; justify-content: center; gap: 16px;
  }
  .brand-square { width: 34px; height: 34px; background: var(--maroon); }
  .brand-name {
    font-family: "Archivo", Arial, sans-serif; font-weight: 800;
    font-size: 38px; letter-spacing: 1px; color: var(--maroon); text-transform: uppercase;
  }

  .label__tagline {
    position: absolute; left: 0; top: 204px; width: 100%; height: 53px;
    display: flex; align-items: center; justify-content: center;
    font-family: "Open Sans", Arial, sans-serif; font-weight: 700;
    font-size: 30px; color: var(--ink-light); letter-spacing: .3px;
  }
  .label__segment {
    position: absolute; left: 0; top: 257px; width: 100%; height: 38px;
    background: var(--slate);
  }
  .segment__rule { position: absolute; top: 18px; height: 2px; background: var(--ink-light); }
  .segment__rule--left { left: 39px; width: 63px; }
  .segment__rule--right { left: 505px; width: 61px; }
  .segment__text {
    position: absolute; left: 0; width: 100%; top: 0; line-height: 38px; text-align: center;
    font-family: "Archivo", Arial, sans-serif; font-weight: 800; font-size: 29px;
    letter-spacing: 1.5px; color: var(--ink-light);
  }

  .contact-frame { position: absolute; left: 0; top: 0; }

  .call-tag {
    position: absolute; left: 89px; top: 339px; width: 25px; height: 57px;
    background: var(--ink-light);
  }
  .call-tag span {
    position: absolute; left: 50%; top: 50%;
    transform: translate(-50%, -50%) rotate(-90deg);
    font-family: "Roboto", Arial, sans-serif; font-weight: 700; font-size: 22px;
    color: var(--maroon); line-height: 1;
  }
  .phone {
    position: absolute; left: 120px; top: 326px;
    font-family: "Roboto Condensed", Arial, sans-serif; font-weight: 700;
    font-size: 64px; line-height: 1; color: var(--ink-light); letter-spacing: .5px;
  }
  .contact-line {
    position: absolute; top: 411px; display: flex; align-items: center; gap: 8px;
    font-size: 24px; color: var(--ink-light); line-height: 30px;
  }
  .contact-line--email { left: 89px; }
  .contact-line--web { left: 355px; }
  .contact-line svg { flex: none; }
</style>
</head>
<body>

<section class="label label--residential">
  <div class="label__brand-area">
    <div class="brand-square"></div>
    <div class="brand-name">Kelz Overhead Door</div>
  </div>
  <div class="label__tagline">The best garage door solutions for</div>
  <div class="label__segment">
    <div class="segment__rule segment__rule--left"></div>
    <div class="segment__text">RESIDENTIAL NEEDS</div>
    <div class="segment__rule segment__rule--right"></div>
  </div>
  <svg class="contact-frame" width="605" height="490" viewBox="0 0 605 490" aria-hidden="true">
    <g fill="none" stroke="#ffffff" stroke-width="5">
      <line x1="39" y1="319" x2="566" y2="319"/>
      <line x1="61" y1="319" x2="61" y2="461"/>
      <polyline points="39,458 563,458 563,388"/>
    </g>
  </svg>
  <div class="call-tag"><span>Call</span></div>
  <div class="phone">(519) 555-0147</div>
  <div class="contact-line contact-line--email">
    <svg width="26" height="22" viewBox="0 0 26 22" aria-hidden="true"><g fill="none" stroke="#fff" stroke-width="1.5"><path d="M1 9 L13 1 L25 9 V21 H1 Z"/><path d="M1 9 L13 16 L25 9"/><path d="M1 21 L10 14 M25 21 L16 14"/></g></svg>
    <span>sales@kelz.ca</span>
  </div>
  <div class="contact-line contact-line--web">
    <svg width="22" height="22" viewBox="0 0 22 22" aria-hidden="true"><g fill="none" stroke="#fff" stroke-width="1.5"><circle cx="11" cy="11" r="9.5"/><ellipse cx="11" cy="11" rx="4.5" ry="9.5"/><line x1="1.5" y1="11" x2="20.5" y2="11"/><line x1="3" y1="6" x2="19" y2="6"/><line x1="3" y1="16" x2="19" y2="16"/></g></svg>
    <span>www.kelz.ca</span>
  </div>
</section>

<section class="label label--commercial">
  <div class="label__brand-area">
    <div class="brand-square"></div>
    <div class="brand-name">Kelz Overhead Door</div>
  </div>
  <div class="label__tagline">The best garage door solutions for</div>
  <div class="label__segment">
    <div class="segment__rule segment__rule--left"></div>
    <div class="segment__text">COMMERCIAL NEEDS</div>
    <div class="segment__rule segment__rule--right"></div>
  </div>
  <svg class="contact-frame" width="605" height="490" viewBox="0 0 605 490" aria-hidden="true">
    <g fill="none" stroke="#ffffff" stroke-width="5">
      <line x1="39" y1="319" x2="566" y2="319"/>
      <line x1="61" y1="319" x2="61" y2="461"/>
      <polyline points="39,458 563,458 563,388"/>
    </g>
  </svg>
  <div class="call-tag"><span>Call</span></div>
  <div class="phone">(519) 555-0147</div>
  <div class="contact-line contact-line--email">
    <svg width="26" height="22" viewBox="0 0 26 22" aria-hidden="true"><g fill="none" stroke="#fff" stroke-width="1.5"><path d="M1 9 L13 1 L25 9 V21 H1 Z"/><path d="M1 9 L13 16 L25 9"/><path d="M1 21 L10 14 M25 21 L16 14"/></g></svg>
    <span>sales@kelz.ca</span>
  </div>
  <div class="contact-line contact-line--web">
    <svg width="22" height="22" viewBox="0 0 22 22" aria-hidden="true"><g fill="none" stroke="#fff" stroke-width="1.5"><circle cx="11" cy="11" r="9.5"/><ellipse cx="11" cy="11" rx="4.5" ry="9.5"/><line x1="1.5" y1="11" x2="20.5" y2="11"/><line x1="3" y1="6" x2="19" y2="6"/><line x1="3" y1="16" x2="19" y2="16"/></g></svg>
    <span>www.kelz.ca</span>
  </div>
</section>

</body>
</html>
```